Business Card Design Project

restaurant management company needs business card design.

Industry/Entity Type

Restaurant

Requirements
Must have
• our logo
pasta nook logo
RWJ logo
WrapDome Logo
Nice to have
• Corwin Tally
(position)

283 Maplerow Street
Larkfield ON,
Canada
K2R 8J4

Tel 555-xxx-xxxx Ext 114
Fax 555-xxx-xxxx
Mobile 555-xxx-xxxx

corwintally@brelvanco.ca
Should not have
• Corwin Tally
(position)

283 Maplerow Street
Larkfield ON,
Canada
K2R 8J4

Tel 555-xxx-xxxx Ext 114
Fax 555-xxx-xxxx
Mobile 555-xxx-xxxx

corwintally@brelvanco.ca

```html
<!DOCTYPE html>
<html lang="en">
<head>
<meta charset="utf-8">
<title>Business Card – Corwin Tally</title>
<link rel="stylesheet" href="https://fonts.googleapis.com/css2?family=Open+Sans:wght@300;400;700;800&display=swap">
<style>
  :root {
    --backdrop: #ececec;
    --card: #ffffff;
    --card-fade: #f1f1f1;
    --ink: #111111;
    --ink-soft: #5a5a5a;
    --accent: #ee1c1c;
    --partner-a: #b3121b;
    --partner-b: #c8102e;
    --partner-c: #3a2a7a;
  }
  * { margin: 0; padding: 0; box-sizing: border-box; }
  html, body {
    width: 1200px;
    height: 900px;
    overflow: hidden;
    background: var(--backdrop);
    font-family: "Open Sans", Arial, sans-serif;
  }
  .card {
    position: absolute;
    left: 162px;
    top: 200px;
    width: 894px;
    height: 510px;
    border-radius: 34px;
    background: linear-gradient(180deg, var(--card) 55%, var(--card-fade) 100%);
    overflow: hidden;
    border: 1px solid #dddddd;
  }
  .card__crescent {
    position: absolute;
    left: 0;
    top: 0;
    width: 894px;
    height: 510px;
  }
  .brand {
    position: absolute;
    left: 34px;
    top: 66px;
    display: flex;
    align-items: center;
    gap: 14px;
  }
  .brand__dot {
    width: 26px;
    height: 26px;
    border-radius: 50%;
    background: var(--accent);
  }
  .brand__name {
    font-size: 30px;
    font-weight: 800;
    color: var(--ink);
    line-height: 1.05;
    letter-spacing: -0.5px;
  }
  .holder {
    position: absolute;
    right: 72px;
    top: 150px;
    text-align: right;
  }
  .holder__name {
    font-size: 31px;
    font-weight: 700;
    color: var(--ink);
    line-height: 1.1;
  }
  .holder__role {
    font-size: 20px;
    font-weight: 400;
    color: var(--ink-soft);
    margin-top: 6px;
  }
  .address {
    position: absolute;
    left: 64px;
    top: 262px;
    font-size: 21px;
    font-weight: 300;
    color: var(--ink-soft);
    line-height: 31px;
    font-style: normal;
  }
  .contact {
    position: absolute;
    left: 64px;
    top: 364px;
    list-style: none;
    font-size: 21px;
    font-weight: 300;
    color: var(--ink-soft);
  }
  .contact__item {
    display: flex;
    align-items: center;
    gap: 10px;
    height: 29.5px;
  }
  .contact__icon {
    width: 22px;
    height: 18px;
    flex: none;
  }
  .partners {
    position: absolute;
    left: 568px;
    top: 420px;
    width: 300px;
    display: flex;
    justify-content: space-between;
    align-items: center;
  }
  .partner {
    font-size: 19px;
    font-weight: 800;
    line-height: 1;
    white-space: nowrap;
  }
  .partner--pasta { color: var(--partner-a); }
  .partner--rwj { color: var(--partner-b); font-size: 24px; }
  .partner--wrap { color: var(--partner-c); }
</style>
</head>
<body>
  <section class="card" aria-label="Business card for Corwin Tally">
    <svg class="card__crescent" viewBox="0 0 894 510" aria-hidden="true">
      <defs>
        <mask id="crescent-cut">
          <rect width="894" height="510" fill="#fff"/>
          <circle cx="768" cy="500" r="215" fill="#000"/>
        </mask>
      </defs>
      <circle cx="716" cy="462" r="224" fill="var(--accent)" mask="url(#crescent-cut)"/>
    </svg>

    <div class="brand">
      <span class="brand__dot" aria-hidden="true"></span>
      <span class="brand__name">Brelvan<br>Management Co</span>
    </div>

    <div class="holder">
      <h1 class="holder__name">Corwin Tally</h1>
      <p class="holder__role">Marketing Manager</p>
    </div>

    <address class="address">
      283 Maplerow Street<br>
      Larkfield ON, Canada K2R 8J4
    </address>

    <ul class="contact">
      <li class="contact__item">
        <svg class="contact__icon" viewBox="0 0 22 18" aria-label="Telephone"><path d="M2 7c0-3 4-5 9-5s9 2 9 5l-4 1-1-2H7L6 8z M5 9h12l2 7H3z" fill="var(--accent)"/><circle cx="11" cy="12" r="2" fill="#fff"/></svg>
        <span>555-xxx-xxxx Ext 114</span>
      </li>
      <li class="contact__item">
        <svg class="contact__icon" viewBox="0 0 22 18" aria-label="Fax"><rect x="6" y="1" width="10" height="5" fill="none" stroke="var(--accent)" stroke-width="1.6"/><rect x="3" y="6" width="16" height="11" rx="1" fill="var(--accent)"/><rect x="6" y="9" width="10" height="1.6" fill="#fff"/><rect x="6" y="12" width="10" height="1.6" fill="#fff"/></svg>
        <span>555-xxx-xxxx</span>
      </li>
      <li class="contact__item">
        <svg class="contact__icon" viewBox="0 0 22 18" aria-label="Mobile"><rect x="4" y="11" width="3" height="6" fill="var(--accent)"/><rect x="8.5" y="8" width="3" height="9" fill="var(--accent)"/><rect x="13" y="5" width="3" height="12" fill="var(--accent)"/><rect x="17.5" y="2" width="3" height="15" fill="var(--accent)"/></svg>
        <span>555-xxx-xxxx</span>
      </li>
      <li class="contact__item">
        <svg class="contact__icon" viewBox="0 0 22 18" aria-label="Email"><rect x="3" y="4" width="16" height="11" fill="none" stroke="var(--accent)" stroke-width="1.6"/><path d="M3 4l8 6 8-6" fill="none" stroke="var(--accent)" stroke-width="1.6"/></svg>
        <span>corwintally@brelvanco.ca</span>
      </li>
    </ul>

    <div class="partners">
      <span class="partner partner--pasta">pasta nook</span>
      <span class="partner partner--rwj">RWJ</span>
      <span class="partner partner--wrap">WrapDome</span>
    </div>
  </section>
</body>
</html>
```